Logo for a recruitment consultancy and executive search firm
The Ashcombe Reeve Partnership
Logo for a recruitment consultancy and executive search firm - Consulting
Creative Brief
Professional
Marian Colbeck
Head of Practice
London office: Belgrove Court 42 Belgrove Court Mayfair London W1K 4PL Dublin office: Block C The Larchfield House Oakpark, Kilbarrow Dublin, 9
marian@ashcombe-reeve.example
www.ashcombe-reeve.example
We will need 3 other business cards details are as follows: Name: Tarek Haddadi Title: Head of Practice Address: London office: Belgrove Court 42 Belgrove Court Mayfair London W1K 4PL Dublin office: Block C The Larchfield House Oakpark, Kilbarrow Dublin, 9 Phone: 020 7946 0321 Mobile: 07700900482 Email: tarek@ashcombe-reeve.example Name: Judith Purcell Title: CEO Address: London office: Belgrove Court 42 Belgrove Court Mayfair London W1K 4PL Dublin office: Block C The Larchfield House Oakpark, Kilbarrow Dublin, 9 Phone: 020 7946 0321 Mobile: 07700 900 615 Email: judith@ashcombe-reeve.example Name: Helen Varty Title: Finance Manager Address: London office: Belgrove Court 42 Belgrove Court Mayfair London W1K 4PL Dublin office: Block C The Larchfield House Oakpark, Kilbarrow Dublin, 9 0321 Mobile: 07700 900 738 email: accounts@ashcombe-reeve.example We want the complete stationary set! The more the merrier as far as I am concerned. folders compliment strips headed paper email signature envelopes presentation format position documents folder you name it we want it!
Black with Ashcombe reeve logo

```html
<!DOCTYPE html>
<html lang="en">
<head>
<meta charset="utf-8">
<title>The Ashcombe Reeve Partnership – Business Card</title>
<link rel="stylesheet" href="https://fonts.googleapis.com/css2?family=Cinzel:wght@400;500&display=swap">
<style>
  :root {
    --backdrop: #e6e3df;
    --card-black: #1d1917;
    --card-white: #f7f6f4;
    --ink-light: #f1eeea;
    --ink-muted: #b9b2ab;
    --ink-grey: #8c8782;
    --rule: #6d6661;
    --shadow: rgba(0,0,0,0.22);
  }
  * { box-sizing: border-box; margin: 0; padding: 0; }
  html, body {
    width: 1200px; height: 989px; overflow: hidden;
    background: var(--backdrop);
    font-family: "Cinzel", "Times New Roman", serif;
  }
  .stage {
    width: 1200px; height: 989px;
    display: flex; flex-direction: column; align-items: center; justify-content: center;
    gap: 48px;
  }
  .card {
    position: relative;
    width: 720px; height: 424px;
    background: var(--card-black);
    box-shadow: 0 10px 28px var(--shadow);
    overflow: hidden;
  }

  /* Back of card */
  .card-back .brand-mark {
    position: absolute; left: 0; right: 0; top: 118px;
    text-align: center; color: var(--ink-light); font-weight: 400;
  }
  .card-back .brand-mark .brand-name { font-size: 38px; letter-spacing: 3px; display: block; }
  .card-back .brand-mark .brand-sub { font-size: 18px; letter-spacing: 5px; display: block; margin-top: 6px; }
  .card-back .web {
    position: absolute; left: 0; right: 0; top: 318px;
    text-align: center; color: var(--ink-muted);
    font-size: 12px; letter-spacing: 5px; text-transform: uppercase;
  }

  /* Front of card */
  .card-front .footer-band {
    position: absolute; left: 0; right: 0; bottom: 0; height: 86px;
    background: var(--card-white);
    border-top: 4px solid var(--rule);
  }
  .card-front .footer-band .web {
    position: absolute; left: 0; right: 0; top: 44px;
    text-align: center; color: var(--ink-grey);
    font-size: 12px; letter-spacing: 6px; text-transform: uppercase;
  }
  .card-front .brand-mark {
    position: absolute; left: 34px; top: 118px; width: 270px;
    text-align: center; color: var(--ink-light); font-weight: 400;
  }
  .card-front .brand-mark .brand-name { display: block; font-size: 27px; letter-spacing: 1px; }
  .card-front .brand-mark .brand-sub { display: block; font-size: 15px; letter-spacing: 4px; margin-top: 6px; }
  .card-front .divider {
    position: absolute; left: 326px; top: 52px; width: 1px; height: 250px;
    background: var(--rule);
  }
  .contact {
    position: absolute; left: 350px; top: 54px; width: 350px;
    color: var(--ink-light);
  }
  .contact .person-name { font-size: 21px; letter-spacing: 1px; }
  .contact .person-title { font-size: 13px; letter-spacing: 1.5px; color: var(--ink-muted); margin-top: 4px; }
  .contact .details { list-style: none; margin-top: 22px; }
  .contact .details li {
    display: flex; align-items: flex-start; gap: 10px;
    font-size: 12.5px; line-height: 1.35; letter-spacing: 0.6px;
    margin-bottom: 7px;
  }
  .contact .icon { flex: 0 0 16px; width: 16px; height: 16px; margin-top: 1px; }
</style>
</head>
<body>
<main class="stage">

  <section class="card card-back" aria-label="Back of business card">
    <div class="brand-mark">
      <span class="brand-name">ASHCOMBE REEVE</span>
      <span class="brand-sub">PARTNERSHIP</span>
    </div>
    <p class="web">www.ashcombe-reeve.example</p>
  </section>

  <section class="card card-front" aria-label="Front of business card">
    <div class="brand-mark">
      <span class="brand-name">ASHCOMBE REEVE</span>
      <span class="brand-sub">PARTNERSHIP</span>
    </div>
    <div class="divider"></div>

    <div class="contact">
      <p class="person-name">Marian Colbeck</p>
      <p class="person-title">Head of Practice</p>
      <ul class="details">
        <li>
          <svg class="icon" viewBox="0 0 16 16" aria-hidden="true"><circle cx="8" cy="8" r="8" fill="#f1eeea"/><path d="M8 3.5a3 3 0 0 0-3 3c0 2.2 3 5.8 3 5.8s3-3.6 3-5.8a3 3 0 0 0-3-3zm0 4.2a1.2 1.2 0 1 1 0-2.4 1.2 1.2 0 0 1 0 2.4z" fill="#1d1917"/></svg>
          <span>Block C The Larchfield House<br>Oakpark, Kilbarrow Dublin, 9</span>
        </li>
        <li>
          <svg class="icon" viewBox="0 0 16 16" aria-hidden="true"><circle cx="8" cy="8" r="8" fill="#f1eeea"/><path d="M5.2 4.2l1.4-.3.9 2-1 .8a6 6 0 0 0 2.8 2.8l.8-1 2 .9-.3 1.4c-.1.4-.5.6-.9.6A7.2 7.2 0 0 1 4.6 5.1c0-.4.2-.8.6-.9z" fill="#1d1917"/></svg>
          <span>020 7946 0321</span>
        </li>
        <li>
          <svg class="icon" viewBox="0 0 16 16" aria-hidden="true"><circle cx="8" cy="8" r="8" fill="#f1eeea"/><rect x="5.6" y="3.5" width="4.8" height="9" rx="0.8" fill="#1d1917"/><rect x="6.4" y="4.6" width="3.2" height="5.6" fill="#f1eeea"/></svg>
          <span>07700900482</span>
        </li>
        <li>
          <svg class="icon" viewBox="0 0 16 16" aria-hidden="true"><circle cx="8" cy="8" r="8" fill="#f1eeea"/><rect x="4" y="5" width="8" height="6" fill="#1d1917"/><path d="M4.3 5.3L8 8.3l3.7-3" stroke="#f1eeea" stroke-width="0.8" fill="none"/></svg>
          <span>marian@ashcombe-reeve.example</span>
        </li>
        <li>
          <svg class="icon" viewBox="0 0 16 16" aria-hidden="true"><circle cx="8" cy="8" r="8" fill="#f1eeea"/><g fill="none" stroke="#1d1917" stroke-width="0.9"><circle cx="8" cy="8" r="4.2"/><ellipse cx="8" cy="8" rx="1.8" ry="4.2"/><path d="M3.8 8h8.4"/></g></svg>
          <span>www.ashcombe-reeve.example</span>
        </li>
      </ul>
    </div>

    <div class="footer-band">
      <p class="web">www.ashcombe-reeve.example</p>
    </div>
  </section>

</main>
</body>
</html>
```